Stationery design for a hip Muslim Travel Agency

We are looking for a colorful and energetic stationery design for a Muslim tour and travel agency. We need a letterhead, A4 folder, business card and loyalty card design.

The designs should be clean and cheerful and have a feeling of a colorful mosaic in a mosque. You can use the Mingleroo avatar and cover photo as the basis.

Pelitaru card is a loyalty card we issue to our clients. This can have a similar feel to the business card and it should NOT have the word "card" added to the logo. Think of airline membership cards.

Target Market(s)

Indonesians, 25-44 years old, Muslim, interesting in Umroh and Haji and other Muslim tours.

Industry/Entity Type

Travel Agent

Contact Information for Business Card

As provided in the .psd file.

Font styles to use
Sans Serif

Colors
27a0d5
33b8a4
00a990
0492cd

Requirements
Must have
• Letterhead design
• A4 folder design
• Business card
• Loyalty card (without the word "card" in the logo)
Nice to have
• Use the mosaic patterns provided in the files. We want to express the theme of colorful Islam.
Should not have
• Don't copy the .psd files provided in the brief. This is just for the content, those files were not prepared by a designer.

```html
<!DOCTYPE html>
<html lang="en">
<head>
<meta charset="utf-8">
<title>Pelitaru Stationery</title>
<link rel="stylesheet" href="https://fonts.googleapis.com/css2?family=Nunito+Sans:wght@400;600;700;800&display=swap">
<style>
  :root {
    --backdrop: #b5b5b5;
    --paper: #eeeeee;
    --ink: #222222;
    --ink-soft: #555555;
    --brand-dark: #333333;
    --teal: #33b8a4;
    --lime: #98c441;
    --lime-deep: #8bb83a;
    --divider: #c8c8c8;
  }
  * { margin: 0; padding: 0; box-sizing: border-box; }
  html, body { width: 1200px; height: 1128px; overflow: hidden; }
  body {
    background: var(--backdrop);
    font-family: "Nunito Sans", Arial, sans-serif;
    color: var(--ink);
    position: relative;
  }

  .brand { display: flex; align-items: center; gap: 7px; font-weight: 800; color: var(--brand-dark); letter-spacing: 0.5px; }
  .brand-dot { border-radius: 50%; background: var(--teal); flex: none; }

  /* Letterhead */
  .letterhead {
    position: absolute; left: 94px; top: 112px; width: 642px; height: 910px;
    background: var(--paper); box-shadow: 0 2px 6px rgba(0,0,0,0.25);
  }
  .letterhead .brand { position: absolute; left: 56px; top: 62px; font-size: 28px; }
  .letterhead .brand-dot { width: 40px; height: 40px; }
  .letterhead-address {
    position: absolute; right: 55px; top: 63px; text-align: right;
    font-size: 9px; line-height: 14.4px; color: var(--ink);
  }
  .letter-body {
    position: absolute; left: 56px; top: 262px; width: 531px;
    font-size: 10.4px; line-height: 17.6px; text-align: justify;
  }
  .letter-body p { margin-bottom: 17.6px; }
  .letter-signoff { position: absolute; left: 56px; top: 596px; font-size: 10.4px; line-height: 17.6px; }
  .signature { position: absolute; left: 458px; top: 648px; width: 120px; height: 76px; background: #e4e4e4; border-radius: 4px; }
  .letter-contacts {
    position: absolute; left: 56px; right: 55px; top: 849px;
    display: flex; justify-content: space-between; align-items: center;
    font-size: 10.4px;
  }
  .contact-item { display: flex; align-items: center; gap: 6px; }
  .contact-divider { width: 1px; height: 18px; background: var(--divider); }
  .icon-mark { width: 9px; height: 9px; border-radius: 50%; background: var(--lime); }
  .band { position: absolute; left: 0; right: 0; bottom: 0; height: 26px; background: var(--lime); }

  /* Business card front */
  .card-front {
    position: absolute; left: 778px; top: 620px; width: 335px; height: 184px;
    background: var(--paper); box-shadow: 0 2px 5px rgba(0,0,0,0.25);
  }
  .card-front .brand { position: absolute; left: 15px; top: 13px; font-size: 17px; gap: 5px; }
  .card-front .brand-dot { width: 24px; height: 24px; }
  .card-name { position: absolute; left: 48px; top: 89px; font-size: 11.5px; font-weight: 700; color: var(--teal); }
  .card-title { position: absolute; left: 48px; top: 105px; font-size: 8px; color: var(--ink-soft); }
  .card-contacts { position: absolute; left: 48px; top: 135px; font-size: 6.6px; line-height: 12px; color: var(--ink-soft); }
  .card-contacts div { display: flex; align-items: center; gap: 5px; }
  .card-address { position: absolute; right: 17px; top: 135px; text-align: right; font-size: 6.6px; line-height: 12px; color: var(--ink-soft); }
  .card-front .band { height: 13px; }

  /* Business card back */
  .card-back {
    position: absolute; left: 782px; top: 838px; width: 334px; height: 186px;
    background: var(--lime); box-shadow: 0 2px 5px rgba(0,0,0,0.25);
    display: flex; align-items: center; justify-content: center;
  }
  .card-back .brand { color: #f4f8ea; font-size: 30px; gap: 12px; }
  .card-back .brand-dot { width: 48px; height: 48px; background: #f4f8ea; }
</style>
</head>
<body>

<section class="letterhead">
  <div class="brand"><span class="brand-dot"></span>pelitaru.id</div>
  <address class="letterhead-address" style="font-style:normal">
    Jl. Kenari Raya No. 21, Cempaka Barat<br>
    Menteng Dalam, Jakarta Pusat 10340<br>
    0888-PELITARU (7354827)
  </address>

  <div class="letter-body">
    <p>Dear Human,</p>
    <p>Cras venenatis, ex ut rhoncus semper, velit dolor finius dui, egeteces volutpat celerisque luctus dolor sit amet, consectetur.</p>
    <p>elit dui nec lectus. Suspendisse facilisis lacus ligula, et viverra ectus laoreet vel. Morbi ullamcorper urna semper, accumsan nulla eu, iaculis lacus. Nunc iaculis arcu a scelerisque luctus. Lorem ipsum dolor sit amet, consectetur adipiscing elit. Aliquam ut tempor dolor, id varius ante. Sed interdum siterz amet nulla venenatis suscipit. Nunc tellus ipsum, fermentum quis interdum non, posuere imperdiet nibh. Vivamus avec faucibus et dui ut laoreet. Aves Aliquam scelerisque lectus metus, nec aue interdum odio volutpat egetex. Nullam a arcu ac ex volutpat tempus. Phasellus at pharetra tortor, euro convallis mauris.</p>
    <p>Vestibulum dictum volutpat magna non ultricies.Praesent rncus ligula ex, ac venenatis felis tincidunt id. Sed aliquet sed odio in tristique. Sed sedex ullamcorper velit. Class aptent taciti sociosqu ad litora torquent per conubia nostra, per inceptos himenaeos. Mauris bibendum in felis zero egestase faucibus. Curabitur sollicitudin varius lorem id semper. Faucibus et dui ut laoreet. Aliquam scelerisque lectus metus, nec aue interdum odio volutpat eget. Nullam a arcu ac ex volutpat tempus. Phasellus at pharetra tortoru convallis mauris.</p>
  </div>

  <div class="letter-signoff">Ratna Wulandari<br>Chairman</div>
  <div class="signature" role="img" aria-label="Handwritten signature"></div>

  <div class="letter-contacts">
    <span class="contact-item">
      <svg width="12" height="9" viewBox="0 0 12 9"><rect width="12" height="9" fill="#98c441"/><path d="M0 0 L6 5 L12 0" fill="none" stroke="#eeeeee" stroke-width="1"/></svg>
      salam@pelitaru.id
    </span>
    <span class="contact-divider"></span>
    <span class="contact-item"><span class="icon-mark"></span>Mingleroo: Pelitaru</span>
    <span class="contact-divider"></span>
    <span class="contact-item"><span class="icon-mark"></span>pelitaru.id</span>
    <span class="contact-divider"></span>
    <span class="contact-item"><span class="icon-mark"></span>Pelitaru Indonesia</span>
  </div>
  <div class="band"></div>
</section>

<section class="card-front">
  <div class="brand"><span class="brand-dot"></span>pelitaru.id</div>
  <div class="card-name">Fajar Hidayat Saputra</div>
  <div class="card-title">General Manager</div>
  <div class="card-contacts">
    <div>
      <svg width="7" height="7" viewBox="0 0 10 10"><path d="M2 0 L4 3 L3 4 Q4.5 6 6 7 L7 6 L10 8 L8.5 10 Q2 9 0 1.5 Z" fill="#98c441"/></svg>
      +62 8800417263
    </div>
    <div>
      <svg width="7" height="6" viewBox="0 0 12 9"><rect width="12" height="9" fill="none" stroke="#98c441" stroke-width="1.5"/><path d="M0 0 L6 5 L12 0" fill="none" stroke="#98c441" stroke-width="1.2"/></svg>
      fajarsaputra@pelitaru.id
    </div>
  </div>
  <div class="card-address">Jl. Kenari Raya No. 21 Cempaka Barat<br>Menteng Dalam, Jakarta Pusat, 10340</div>
  <div class="band"></div>
</section>

<section class="card-back">
  <div class="brand"><span class="brand-dot"></span>pelitaru.id</div>
</section>

</body>
</html>
```